Design a Travel and Tourism website

We would like a freelancer to design a website that is essentially easy to use and navigate database providing local information for Travelers about destination countries.

We proposed website would discuss different rates, fees, visa requirement, resort locations, cheap flights, etc. This website should be elegant and modern. Our business name is mirdalon.
Some reference websites are plendavix.ca, gosthandiverquo.com,
There should be a forum in the website where travell\ers discuss about their first hand tranvel experience to such destinations.

```html
<!DOCTYPE html>
<html lang="en">
<head>
<meta charset="utf-8">
<title>Mirdalon — find your adventure</title>
<link rel="stylesheet" href="https://fonts.googleapis.com/css2?family=Nunito+Sans:wght@300;400;600;700&display=swap">
<style>
  :root {
    --ink: #4d566f;
    --ink-soft: #66708c;
    --muted: #9a9ea8;
    --line: #e3e4e6;
    --paper: #ffffff;
    --header-bg: #fbfbfa;
    --mist-top: #fafaf8;
    --mist-bottom: #eceeec;
    --photo-top: #7f9a8c;
    --photo-mid: #4d5a52;
    --photo-bottom: #2c2d34;
    --white: #ffffff;
    --headline-faint: #e9e9e8;
  }
  * { box-sizing: border-box; margin: 0; padding: 0; }
  html, body { width: 1200px; height: 1200px; overflow: hidden; background: var(--paper); }
  body { font-family: "Nunito Sans", sans-serif; color: var(--ink); position: relative; }

  .site-header {
    position: absolute; left: 0; top: 0; width: 1200px; height: 123px;
    background: var(--header-bg); border-bottom: 1px solid var(--line);
  }
  .brand { position: absolute; left: 60px; top: 47px; display: flex; align-items: center; gap: 14px; }
  .brand-dot { width: 34px; height: 34px; border-radius: 50%; background: var(--ink); }
  .brand-name { font-size: 38px; font-weight: 300; letter-spacing: 1px; color: var(--ink); line-height: 1; }
  .lang { position: absolute; left: 332px; top: 67px; font-size: 13px; font-weight: 700; color: var(--ink); display: flex; align-items: center; gap: 4px; }
  .main-nav { position: absolute; top: 60px; left: 679px; display: flex; gap: 0; }
  .main-nav a { color: var(--ink); text-decoration: none; font-size: 19px; font-weight: 400; position: absolute; white-space: nowrap; }
  .close-btn { position: absolute; left: 1102px; top: 56px; }

  .hero { position: absolute; left: 0; top: 124px; width: 1200px; height: 600px; }
  .hero-mist { position: absolute; left: 0; top: 0; width: 1200px; height: 204px;
    background: linear-gradient(180deg, var(--mist-top) 0%, var(--mist-top) 55%, var(--mist-bottom) 100%); }
  .hero-photo { position: absolute; left: 0; top: 204px; width: 1200px; height: 396px;
    background: linear-gradient(180deg, var(--photo-top) 0%, var(--photo-mid) 35%, var(--photo-bottom) 100%); }
  .hero-title { position: absolute; left: 0; width: 1200px; top: 48px; text-align: center;
    font-size: 64px; font-weight: 300; letter-spacing: 3px; color: var(--headline-faint); }
  .side-links { position: absolute; right: 66px; top: 48px; text-align: right; list-style: none; }
  .side-links li { font-size: 12px; color: var(--ink); height: 37px; }

  .search-tabs { position: absolute; left: 67px; top: 263px; width: 195px; height: 36px;
    border: 1px solid var(--white); border-radius: 6px; display: flex; overflow: hidden; }
  .search-tabs span { font-size: 16px; font-weight: 700; display: flex; align-items: center; justify-content: center; }
  .tab-active { width: 92px; background: var(--white); color: var(--ink); border-radius: 5px; }
  .tab { flex: 1; color: var(--white); }

  .field { position: absolute; top: 352px; transform: translateX(-50%); text-align: center; color: var(--white); white-space: nowrap; }
  .field-label { font-size: 14px; font-weight: 700; letter-spacing: 1px; display: block; }
  .field-label small { font-size: 12px; font-weight: 400; letter-spacing: 0; }
  .field-value { font-size: 16px; font-weight: 400; display: block; margin-top: 3px; }
  .field-value svg { margin-left: 20px; vertical-align: middle; }

  .search-btn { position: absolute; left: 974px; top: 333px; width: 160px; height: 72px;
    border: 2px solid var(--white); border-radius: 6px; color: var(--white);
    font-size: 20px; font-weight: 700; display: flex; align-items: center; justify-content: center; }

  .story { position: absolute; left: 0; top: 690px; width: 1200px; text-align: center; }
  .author-photo { width: 78px; height: 78px; border-radius: 50%; margin: 0 auto;
    background: linear-gradient(160deg, #b98a6a, #e2c3ad); border: 4px solid var(--white); }
  .author { font-size: 15px; font-weight: 700; color: var(--ink-soft); margin-top: 6px; }
  .place { font-size: 14px; letter-spacing: 3px; color: var(--muted); margin-top: 14px; }
  .story-title { font-size: 43px; font-weight: 300; color: var(--ink); margin-top: 62px; }
  .story-text { font-size: 17px; line-height: 22px; color: var(--ink-soft); width: 560px; margin: 30px auto 0; }
  .read-more { display: inline-block; margin-top: 22px; font-size: 19px; font-weight: 700; color: var(--ink-soft);
    text-decoration: none; border-bottom: 1px solid var(--ink-soft); line-height: 22px; }
  .carousel-arrow { position: absolute; top: 943px; }
</style>
</head>
<body>
  <header class="site-header">
    <div class="brand"><span class="brand-dot"></span><span class="brand-name">MIRDALON</span></div>
    <div class="lang">FR
      <svg width="13" height="8" viewBox="0 0 13 8"><path d="M1 1l5.5 5.5L12 1" fill="none" stroke="var(--ink)" stroke-width="1.6"/></svg>
    </div>
    <nav class="main-nav">
      <a href="#" style="left:0">resorts</a>
      <a href="#" style="left:86px">flights</a>
      <a href="#" style="left:170px">fees</a>
      <a href="#" style="left:234px">visas</a>
      <a href="#" style="left:303px">login</a>
    </nav>
    <svg class="close-btn" width="30" height="30" viewBox="0 0 30 30" aria-label="close menu">
      <path d="M1 1l28 28M29 1L1 29" stroke="var(--ink)" stroke-width="1.8"/>
    </svg>
  </header>

  <section class="hero">
    <div class="hero-mist" role="img" aria-label="Misty mountain ridges fading into a pale sky"></div>
    <div class="hero-photo" role="img" aria-label="Green mountain valley seen from a rocky ledge with a hiker holding a trekking pole"></div>
    <h1 class="hero-title">find your adventure</h1>
    <ul class="side-links">
      <li>sign up</li>
      <li>our destinations</li>
      <li>traveler forum</li>
    </ul>

    <div class="search-tabs"><span class="tab-active">flights</span><span class="tab">resorts</span></div>

    <div class="field" style="left:113px"><span class="field-label">FROM</span><span class="field-value">enter airport</span></div>
    <div class="field" style="left:262px"><span class="field-label">TO</span><span class="field-value">enter airport</span></div>
    <div class="field" style="left:406px"><span class="field-label">DEPART</span><span class="field-value">dd / mm / yy</span></div>
    <div class="field" style="left:553px"><span class="field-label">RETURN</span><span class="field-value">dd / mm / yy</span></div>
    <div class="field" style="left:683px"><span class="field-label">ADULTS</span><span class="field-value">1<svg width="12" height="7" viewBox="0 0 12 7"><path d="M1 1l5 5 5-5" fill="none" stroke="#fff" stroke-width="1"/></svg></span></div>
    <div class="field" style="left:836px"><span class="field-label">CHILDREN <small>( under 17 )</small></span><span class="field-value">0<svg width="12" height="7" viewBox="0 0 12 7"><path d="M1 1l5 5 5-5" fill="none" stroke="#fff" stroke-width="1"/></svg></span></div>

    <div class="search-btn">search</div>
  </section>

  <section class="story">
    <div class="author-photo" role="img" aria-label="Portrait of the story author"></div>
    <p class="author">by janedoe</p>
    <p class="place">SCOTLAND</p>
    <h2 class="story-title">Share Your Story</h2>
    <p class="story-text">Lorem ipsum dolor sit amet, consectetur adipisicing elit, sed do eiusmod tempor incididunt ut labore et dolore magna aliqua.</p>
    <a class="read-more" href="#">Read more</a>
  </section>

  <svg class="carousel-arrow" style="left:90px" width="46" height="86" viewBox="0 0 46 86" aria-label="previous story">
    <path d="M45 1L2 43l43 42" fill="none" stroke="#c9cbd8" stroke-width="1.5"/>
  </svg>
  <svg class="carousel-arrow" style="left:1063px" width="46" height="86" viewBox="0 0 46 86" aria-label="next story">
    <path d="M1 1l43 42L1 85" fill="none" stroke="#c9cbd8" stroke-width="1.5"/>
  </svg>
</body>
</html>
```